Corvane: The Quiet Lantern

I need a front, back and spine cover for e and print for a short book. The book is called Corvane, subtitle, The Quiet Lantern. It is about an eyewitness to the Archangel Corvane. I would like to use the design many times with different colours for a series in spirituality and magic. So hopefully I can work with the designer again. The simple idea, is a plain cover in a colour, here blue. Mostly a font based cover, with a small symbolic image silhouetted at the bottom. Other covers will be orange, same font, and a different silhouette symbolic image and so on.

We need: a blue that will print well and look good on a screen. Serious, inviting honesty and truth and not flat. A font that is modern, female, says mystic but not old saint. The author is female and an award-winning writer in different areas. We need a uniform space for a title, (here Corvane), a uniform space for "The Quiet Lantern", a small space for a simple symbolic image, and author name, Wren Halloway. The small image on this blue cover should be in red. Ideas would be a simple rose head. The cover must look modern and professional and compliment the brand at www.wrenhalloway-books.com.

If the designer would simultaneously like to pitch to design the whole series (which will have many titles), another one would be a warm/hot pink background with the title Blue Harbour, subtitle, Brighten Every Ordinary Week. Small image silhouetted in orange might be a small gift shape, or a seahorse. Same author name, Wren Halloway. Another cover would be green background, title Lanterns: subtitle, Seven Rivers Beyond the Hill. Image in yellow: a rolled yoga mat, or an Om symbol. Wren Halloway. If we find a groove for the whole series, I can keep working with the same designer. Of course, the cover just for Corvane is fine here, but please bear in mind it fits into this wider series. Blue covers are about conversation with or contact with key spiritual figures, each from the author's own personal experience. Another one there would be "Swami Dhorelan", Letters From a Northern Garden. Image would be a simple daisy or a trophy emblem in red.

Font is crucial here and will define a series. Modern spirituality for the current generation. It must suggest contact with higher planes without being chintzy. Thank you!

Simple designs are iconic. That is what we are going for!

Good luck.

Target Market(s)

The people who read iconic series books like old marlow classics

Colors
34a6d7

Requirements
Must have
• modern, iconic, translatable into different markets.
Nice to have
• symbolic images silhouetted into a colour, not black, as the guidelines.
Should not have
• not too emotional.

```html
<!DOCTYPE html>
<html lang="en">
<head>
<meta charset="utf-8">
<title>Corvane: The Quiet Lantern — Cover Wrap</title>
<link href="https://fonts.googleapis.com/css2?family=Cinzel:wght@400;500&family=Cormorant+Garamond:wght@400;500&display=swap" rel="stylesheet">
<style>
  :root {
    --backdrop: #d9f0fb;
    --cover-top: #42addd;
    --cover-mid: #34a6d7;
    --cover-bottom: #166aa2;
    --spine-top: #3aa2d3;
    --spine-bottom: #125f94;
    --ink: #ffffff;
    --ink-soft: rgba(255, 255, 255, 0.85);
    --rose: #c4161c;
    --rose-deep: #8e0d12;
  }

  * { box-sizing: border-box; margin: 0; padding: 0; }

  html, body {
    width: 1200px;
    height: 800px;
    overflow: hidden;
    background: var(--backdrop);
  }

  .cover-wrap {
    position: absolute;
    left: 220px;
    top: 120px;
    width: 760px;
    height: 560px;
    display: flex;
    box-shadow: 0 18px 40px rgba(20, 70, 110, 0.18);
  }

  .panel {
    position: relative;
    height: 100%;
    background: linear-gradient(180deg, var(--cover-top) 0%, var(--cover-mid) 45%, var(--cover-bottom) 100%);
    color: var(--ink);
    text-align: center;
  }

  .back-cover, .front-cover { width: 370px; }

  .spine {
    width: 20px;
    background: linear-gradient(180deg, var(--spine-top), var(--spine-bottom));
    display: flex;
    justify-content: center;
    align-items: center;
    border-left: 1px solid rgba(255,255,255,0.12);
    border-right: 1px solid rgba(0,0,0,0.12);
  }

  .spine-text {
    writing-mode: vertical-rl;
    display: flex;
    align-items: center;
    gap: 34px;
    color: var(--ink-soft);
    white-space: nowrap;
  }

  .spine-title { font-family: "Cinzel", serif; font-size: 13px; letter-spacing: 1px; }
  .spine-subtitle { font-family: "Cormorant Garamond", serif; font-size: 9px; letter-spacing: 1px; }
  .spine-author { font-family: "Cinzel", serif; font-size: 10px; letter-spacing: 2px; margin-top: 110px; }

  /* Front cover */
  .front-title {
    position: absolute;
    top: 92px;
    left: 0; right: 0;
    font-family: "Cinzel", serif;
    font-weight: 400;
    font-size: 60px;
    line-height: 1;
    letter-spacing: 1px;
  }

  .front-subtitle {
    position: absolute;
    top: 172px;
    left: 0; right: 0;
    font-family: "Cormorant Garamond", serif;
    font-size: 19px;
    letter-spacing: 1.5px;
    color: var(--ink-soft);
  }

  .symbol-image {
    position: absolute;
    left: 60px;
    top: 276px;
    width: 250px;
    height: 220px;
    border-radius: 48% 48% 40% 40%;
    background: radial-gradient(ellipse at 50% 40%, var(--rose) 0%, var(--rose) 45%, var(--rose-deep) 100%);
  }

  .front-author {
    position: absolute;
    bottom: 28px;
    left: 0; right: 0;
    font-family: "Cinzel", serif;
    font-size: 31px;
    letter-spacing: 1px;
  }

  /* Back cover */
  .back-title {
    position: absolute;
    top: 180px;
    left: 0; right: 0;
    font-family: "Cinzel", serif;
    font-size: 20px;
  }

  .back-subtitle {
    position: absolute;
    top: 206px;
    left: 0; right: 0;
    font-family: "Cormorant Garamond", serif;
    font-size: 8px;
    letter-spacing: 0.5px;
    color: var(--ink-soft);
  }

  .back-blurb {
    position: absolute;
    top: 246px;
    left: 46px; right: 46px;
    font-family: "Cormorant Garamond", serif;
    font-size: 9.5px;
    line-height: 1.45;
    letter-spacing: 0.4px;
    color: var(--ink-soft);
  }
</style>
</head>
<body>
  <main class="cover-wrap">
    <section class="panel back-cover">
      <h2 class="back-title">Corvane</h2>
      <p class="back-subtitle">The Quiet Lantern</p>
      <p class="back-blurb">A quiet account of one woman's meeting with a presence of light, told with plain honesty and care. Across a handful of short chapters, the author traces the days before and after, the doubts she carried, and the calm that followed. This is a gentle book for readers who keep asking what lies beyond the ordinary, and who trust a lantern held steady in the dark.</p>
    </section>

    <section class="spine">
      <div class="spine-text">
        <span class="spine-title">Corvane</span>
        <span class="spine-subtitle">The Quiet Lantern</span>
        <span class="spine-author">WREN HALLOWAY</span>
      </div>
    </section>

    <section class="panel front-cover">
      <h1 class="front-title">Corvane</h1>
      <p class="front-subtitle">The Quiet Lantern</p>
      <div class="symbol-image" role="img" aria-label="Red rose head on a short dark stem"></div>
      <p class="front-author">WREN HALLOWAY</p>
    </section>
  </main>
</body>
</html>
```